Car rental website design for a UAE car rental company

This project is about creating a new website design for a car rental company located in Dubai (United Arab Emirates), I opened the same project a few months ago but I didn't receive a lot of appealing entries so I closed it but this time I am marking the project as guaranteed to avoid such situation again, if you have already provided a design before then please re-submit again on this project so that it is considered while reviewing all the designs

A few important things:

1- We need a simple non-complex design
2- The final deliverable would be 2 screens (PSD, JPEG ... etc), the first screen is for the home page and the second screen is for an internal page
3- The home page must have a section that end users can use to rent a car online directly from the home page instead of going into some inner pages
4- The current website is very old and not very appealing so avoid creating a similar design (www.quarvin-drive.example)
5- The name is Quarvin but the company rents normal cars (no Limousin cars will be rented) so avoid adding any fancy cars in the images/graphics used in the design, just normal end users cars
6- The expected pages would be: home, About us, Our team, Strategy, Contact us and links to social media pages
7- The attachments include the company's logo and some screens from other car rental companies that provide online rentals/payments

If you have any questions please feel free to ask and please note that we will need the designs urgently

Thanks

Target Market(s)

Dubai - United Arab Emirates

Industry/Entity Type

It Company

Number of Pages Required

2 page

Font styles to use
Sans Serif

Requirements
Must have
• Check the project details
Nice to have
Should not have

```html
<!DOCTYPE html>
<html lang="en">
<head>
<meta charset="utf-8">
<title>Quarvin – Car Rental Dubai</title>
<link rel="stylesheet" href="https://fonts.googleapis.com/css2?family=Open+Sans:ital,wght@0,400;0,600;0,700;1,400;1,600&family=Quicksand:wght@500;700&display=swap">
<style>
:root{
  --red:#a6052f;
  --red-panel:#930329;
  --red-field:#7c0123;
  --red-dark:#6e001d;
  --ink:#222;
  --muted:#555;
  --night:#1b1b1d;
  --footer:#161617;
  --white:#fff;
  --sans:"Open Sans", Arial, sans-serif;
  --round:"Quicksand", "Open Sans", sans-serif;
}
*{box-sizing:border-box;margin:0;padding:0}
html,body{width:740px;height:1200px;overflow:hidden}
body{position:relative;font-family:var(--sans);color:var(--ink);background:var(--white)}

/* Header */
.site-header{position:absolute;left:0;top:0;width:740px;height:60px;background:rgba(20,20,22,.82);z-index:3}
.brand{position:absolute;left:62px;top:12px;display:flex;align-items:center;gap:8px;color:var(--white);font-weight:700;font-size:17px}
.brand-mark{width:24px;height:24px;background:var(--red)}
.topbar{position:absolute;right:63px;top:12px;display:flex;align-items:center;gap:6px;font-size:8.5px;color:#ddd}
.topbar .support{color:#d3163f}
.topbar .follow{margin-left:14px}
.social-dot{width:14px;height:14px;border-radius:50%;background:#c8102e}
.main-nav{position:absolute;right:46px;top:38px;display:flex;gap:0;font-size:8.5px;font-weight:600;color:#eee;letter-spacing:.2px}
.main-nav a{color:inherit;text-decoration:none;margin-left:36px}

/* Hero */
.hero{position:absolute;left:0;top:0;width:740px;height:373px;background:linear-gradient(180deg,#3a3f48 0%,#5a5e66 35%,#2a2c30 65%,#1a1a1c 100%)}
.hero-photo{position:absolute;inset:0;background:radial-gradient(ellipse 260px 110px at 420px 250px,#0c0c0e 0%,rgba(12,12,14,.7) 60%,transparent 100%)}
.hero-caption{position:absolute;left:192px;top:172px;width:342px;height:84px;background:rgba(40,40,44,.45);text-align:center;color:var(--white)}
.hero-caption h1{font-family:var(--round);font-weight:700;font-size:20px;margin-top:10px}
.hero-caption p{font-family:var(--round);font-weight:500;font-size:11px;line-height:17px;margin-top:6px}
.hero-arrow{position:absolute;top:208px}
.hero-arrow.prev{left:50px}
.hero-arrow.next{right:50px}

/* Welcome */
.welcome{position:absolute;left:0;top:373px;width:740px;height:247px;background:var(--white)}
.section-title{font-weight:700;font-size:15px;color:var(--red);text-align:center;letter-spacing:.3px}
.welcome .section-title{margin-top:31px}
.title-rule{display:block;margin:5px auto 0;width:180px;height:1.5px;background:var(--red)}
.welcome-car{position:absolute;left:77px;top:80px;width:238px;height:107px;background:radial-gradient(ellipse 120px 50px at 50% 50%,#2c3a8a 0%,#4c5fb0 55%,rgba(255,255,255,0) 100%);border-radius:40px}
.welcome-text{position:absolute;left:363px;top:91px;width:292px}
.welcome-text .lead{font-style:italic;font-weight:600;font-size:7.6px;line-height:12px;color:#333;text-transform:uppercase}
.welcome-text .body{font-size:7.6px;line-height:12px;color:var(--muted);margin-top:12px}
.btn{display:inline-block;font-size:8.5px;color:var(--white);text-align:center;text-decoration:none}
.btn-red{position:absolute;left:363px;top:186px;width:79px;height:25px;line-height:25px;background:var(--red)}

/* Mission & booking */
.mission-band{position:absolute;left:0;top:620px;width:740px;height:317px;background:var(--red);color:var(--white)}
.band-title{position:absolute;top:19px;font-weight:700;font-size:13.5px;letter-spacing:.2px}
.mission .band-title{left:89px}
.mission-photo{position:absolute;left:89px;top:45px;width:311px;height:128px;border-radius:3px;background:linear-gradient(160deg,#8a8f96 0%,#3e3f44 45%,#1d1d20 70%,#5a0a14 100%)}
.mission-text{position:absolute;left:89px;top:186px;width:272px;font-size:8px;line-height:14px}
.btn-dark{position:absolute;left:89px;top:247px;width:79px;height:25px;line-height:25px;background:var(--red-dark)}
.booking .band-title{left:437px}
.booking-panel{position:absolute;left:441px;top:45px;width:199px;height:251px;background:var(--red-panel);padding:0 20px 0 12px}
.group-label{position:absolute;left:18px;font-size:8px;color:#f4dbe1}
.field{position:absolute;left:12px;width:167px;height:16px;background:var(--red-field);font-size:6.6px;color:#f3d6de;padding:0 8px;line-height:16px}
.field svg{position:absolute;right:6px;top:5px}
.radios{position:absolute;left:18px;font-size:6.6px;color:#f3d6de;display:flex;gap:8px}
.radios span::before{content:"";display:inline-block;width:6px;height:6px;border-radius:50%;background:#f3d6de;margin-right:3px;vertical-align:-1px}
.small-label{position:absolute;font-size:6.4px;color:#f3d6de}
.date{position:absolute;width:67px;height:17px;background:var(--red-field);font-size:6.8px;color:#f3d6de;line-height:17px;padding-left:8px}
.cal{position:absolute}

/* Strip */
.promo{position:absolute;left:0;top:937px;width:740px;height:214px;background:linear-gradient(110deg,#2a2a2d 0%,#161618 45%,#232326 100%);color:var(--white);text-align:center}
.promo-photo{position:absolute;left:60px;top:40px;width:420px;height:170px;background:radial-gradient(ellipse 200px 80px at 50% 60%,rgba(90,10,20,.45),transparent 70%)}
.promo h2{position:relative;font-family:var(--round);font-weight:700;font-size:15px;margin-top:42px}
.promo .title-rule{background:var(--white);width:136px}
.promo p{position:relative;width:530px;margin:11px auto 0;font-size:8px;line-height:13px}
.btn-ghost{position:absolute;left:316px;top:139px;width:109px;height:29px;line-height:27px;border:1px solid #ccc;font-size:7.8px}

/* Footer */
.site-footer{position:absolute;left:0;top:1151px;width:740px;height:49px;background:var(--footer);color:#e6e6e6;font-size:7.8px}
.footer-nav{position:absolute;left:63px;top:19px}
.footer-nav a{color:inherit;text-decoration:none}
.footer-nav .sep{margin:0 4px}
.copyright{position:absolute;right:63px;top:19px}
</style>
</head>
<body>

<section class="hero">
  <div class="hero-photo" role="img" aria-label="Dark sedan parked on a waterfront at dusk with a city skyline behind"></div>
  <div class="hero-caption">
    <h1>We Keep on Developing our abilities</h1>
    <p>And enhancing our Knowledge to ensure that our<br>clients will get only the best from us.</p>
  </div>
  <svg class="hero-arrow prev" width="12" height="18" viewBox="0 0 12 18"><path d="M10 2 3 9l7 7" fill="none" stroke="#fff" stroke-width="2.4"/></svg>
  <svg class="hero-arrow next" width="12" height="18" viewBox="0 0 12 18"><path d="M2 2l7 7-7 7" fill="none" stroke="#fff" stroke-width="2.4"/></svg>
</section>

<header class="site-header">
  <div class="brand"><span class="brand-mark"></span>Quarvin</div>
  <div class="topbar">
    <span class="support">Phone Support :</span><span>+971 4555 0192</span>
    <span class="follow">Follow Us :</span>
    <span class="social-dot"></span><span class="social-dot"></span><span class="social-dot"></span>
  </div>
  <nav class="main-nav">
    <a href="#">HOME</a><a href="#">ABOUT US</a><a href="#">OUR TEAM</a><a href="#">STRATEGY</a><a href="#">CONTACT US</a>
  </nav>
</header>

<section class="welcome">
  <h2 class="section-title">WELCOME TO QUARVIN</h2>
  <span class="title-rule"></span>
  <div class="welcome-car" role="img" aria-label="Blue family estate car"></div>
  <div class="welcome-text">
    <p class="lead">As Dubai is expected to welcome millions of tourists and visitors, car rental industry is believed to escalate more rapidly in the region.</p>
    <p class="body">Over the past five years, demands for car rentals in Dubai has been augmenting at a healthy pace and is currently registering a growth rate of 20 to 25 percent per year. The swift economic growth and the number....</p>
  </div>
  <a class="btn btn-red" href="#">Read More</a>
</section>

<section class="mission-band">
  <div class="mission">
    <h2 class="band-title">MISSION &amp; VISSION</h2>
    <div class="mission-photo" role="img" aria-label="Red car driving on a mountain road under a cloudy sky"></div>
    <p class="mission-text">To be one of the leading auto leasing company in the fast growing economy and tourism industry of the emirate of Dubai and play alongside....</p>
    <a class="btn btn-dark" href="#">Read More</a>
  </div>

  <div class="booking">
    <h2 class="band-title">BOOK CAR HIRE ONLINE</h2>
    <form class="booking-panel">
      <span class="group-label" style="top:9px">Pick Up Location</span>
      <div class="field" style="top:24px">City<svg width="7" height="5" viewBox="0 0 7 5"><path d="M.5.5 3.5 4 6.5.5" fill="none" stroke="#f3d6de" stroke-width="1.3"/></svg></div>
      <div class="radios" style="top:47px"><span>Airport</span><span>City</span></div>
      <div class="field" style="top:62px">Select Your City<svg width="7" height="5" viewBox="0 0 7 5"><path d="M.5.5 3.5 4 6.5.5" fill="none" stroke="#f3d6de" stroke-width="1.3"/></svg></div>
      <span class="small-label" style="left:23px;top:87px">Pick Up Date</span>
      <span class="small-label" style="left:119px;top:87px">Pick Up Time</span>
      <div class="date" style="left:12px;top:99px">26-02-2015</div>
      <svg class="cal" style="left:84px;top:98px" width="19" height="19" viewBox="0 0 19 19"><rect x="1" y="2.5" width="17" height="15" fill="none" stroke="#fff" stroke-width="1.3"/><path d="M1 6.5h17" stroke="#fff" stroke-width="1.3"/><g fill="#fff"><rect x="4" y="9" width="2" height="2"/><rect x="8.5" y="9" width="2" height="2"/><rect x="13" y="9" width="2" height="2"/><rect x="4" y="13" width="2" height="2"/><rect x="8.5" y="13" width="2" height="2"/><rect x="13" y="13" width="2" height="2"/></g></svg>
      <div class="date" style="left:112px;top:99px">26-02-2015</div>

      <span class="group-label" style="top:128px">Drop Off Location</span>
      <div class="field" style="top:143px">City<svg width="7" height="5" viewBox="0 0 7 5"><path d="M.5.5 3.5 4 6.5.5" fill="none" stroke="#f3d6de" stroke-width="1.3"/></svg></div>
      <div class="radios" style="top:166px"><span>Airport</span><span>City</span></div>
      <div class="field" style="top:181px">Select Your City<svg width="7" height="5" viewBox="0 0 7 5"><path d="M.5.5 3.5 4 6.5.5" fill="none" stroke="#f3d6de" stroke-width="1.3"/></svg></div>
      <span class="small-label" style="left:23px;top:206px">Pick Up Date</span>
      <span class="small-label" style="left:119px;top:206px">Pick Up Time</span>
      <div class="date" style="left:12px;top:218px">26-02-2015</div>
      <svg class="cal" style="left:84px;top:217px" width="19" height="19" viewBox="0 0 19 19"><rect x="1" y="2.5" width="17" height="15" fill="none" stroke="#fff" stroke-width="1.3"/><path d="M1 6.5h17" stroke="#fff" stroke-width="1.3"/><g fill="#fff"><rect x="4" y="9" width="2" height="2"/><rect x="8.5" y="9" width="2" height="2"/><rect x="13" y="9" width="2" height="2"/><rect x="4" y="13" width="2" height="2"/><rect x="8.5" y="13" width="2" height="2"/><rect x="13" y="13" width="2" height="2"/></g></svg>
      <div class="date" style="left:112px;top:218px">26-02-2015</div>
    </form>
  </div>
</section>

<section class="promo">
  <div class="promo-photo" role="img" aria-label="Red sports car on a dark road, faded into the background"></div>
  <h2>Lorem Ipsum is simply</h2>
  <span class="title-rule"></span>
  <p>Lorem Ipsum is simply dummy text of the printing and typesetting industry. Lorem Ipsum has been the industry's standard dummy text ever since the 1500s, when an unknown printer took a galley of type and scrambled it to make a type specimen book. It has survived not only five centuries,</p>
  <a class="btn btn-ghost" href="#">READ MORE</a>
</section>

<footer class="site-footer">
  <nav class="footer-nav">
    <a href="#">Home</a><span class="sep">|</span><a href="#">About Us</a><span class="sep">|</span><a href="#">Our Team</a><span class="sep">|</span><a href="#">Strategy</a><span class="sep">|</span><a href="#">Contact Us</a>
  </nav>
  <p class="copyright">©Copyright 2011, Quarvin. All rights reserved.</p>
</footer>

</body>
</html>
```